Business Card Design

Consultation for design, construction athletic facilities specializing in synthetic turf systems and all weather running track systems.
Motto "True Owner Representation"
New Company that we'd like to highlight the LOGO first and foremost with the colors of the background and font as primary colors of the card too if possible. I've also attached a typical larger project design layout that could be used in the background to highlight our design and construction specialty.
Website is something we want very noticeable for driving traffic.
Target Market(s)
Athletic Directors, Designers, Government and Military, Contractors
Industry/Entity Type
Construction
Contact Information for Business Card
Peter L. Vandrell CFB, CTB
48317 W 63rd Ave
Harlow Ridge, WA 99482
C +1 503.555.0147
O +1 808.555.0182
Peter@fieldlaneco.example
www.fieldlaneco.example

```html
<!DOCTYPE html>
<html lang="en">
<head>
<meta charset="utf-8">
<title>Solano Field – Business Card</title>
<link href="https://fonts.googleapis.com/css2?family=Titillium+Web:wght@400;600&family=Cinzel:wght@500&display=swap" rel="stylesheet">
<style>
  :root {
    --canvas-bg: #e9e6e1;
    --card-black: #151515;
    --plan-tone-a: #1b1b1b;
    --plan-tone-b: #121212;
    --ink-white: #f4f4f4;
    --ink-soft: #e2e2e2;
    --gold: #f0a623;
    --divider: #4a4a4a;
  }
  html, body {
    margin: 0;
    padding: 0;
    width: 1200px;
    height: 1000px;
    overflow: hidden;
    background: var(--canvas-bg);
  }
  .canvas {
    position: relative;
    width: 1200px;
    height: 1000px;
  }
  .card {
    position: absolute;
    width: 688px;
    height: 402px;
    background: var(--card-black);
    overflow: hidden;
  }
  .card-front { left: 130px; top: 80px; }
  .card-back  { left: 403px; top: 518px; }

  .site-plan {
    position: absolute;
    inset: 0;
    background: linear-gradient(135deg, var(--plan-tone-a), var(--plan-tone-b));
  }

  .brand-name {
    position: absolute;
    font-family: "Titillium Web", sans-serif;
    font-weight: 400;
    color: var(--gold);
    white-space: nowrap;
    display: flex;
    align-items: center;
  }
  .brand-dot {
    display: inline-block;
    border-radius: 50%;
    background: var(--gold);
  }
  .card-front .brand-name {
    left: 150px;
    top: 160px;
    font-size: 60px;
    letter-spacing: 4px;
  }
  .card-front .brand-dot {
    width: 34px;
    height: 34px;
    margin-right: 22px;
  }

  .contact {
    position: absolute;
    left: 56px;
    top: 44px;
    font-family: "Titillium Web", sans-serif;
    color: var(--ink-soft);
  }
  .contact-name {
    margin: 0;
    font-size: 21px;
    font-weight: 600;
    color: var(--ink-white);
    line-height: 30px;
  }
  .contact-credentials {
    margin: 0 0 26px;
    font-size: 20px;
    font-weight: 400;
    color: var(--gold);
    line-height: 28px;
  }
  .contact-address, .contact-lines {
    margin: 0;
    font-size: 17px;
    line-height: 26px;
    font-style: normal;
  }
  .contact-lines { margin-top: 42px; }
  .contact-website {
    display: block;
    margin-top: 22px;
    font-family: "Cinzel", serif;
    font-weight: 500;
    font-size: 18px;
    letter-spacing: 0.5px;
    color: var(--gold);
    text-decoration: none;
  }
  .card-divider {
    position: absolute;
    left: 398px;
    top: 48px;
    width: 1px;
    height: 306px;
    background: var(--divider);
  }
  .card-back .brand-name {
    left: 440px;
    top: 176px;
    font-size: 26px;
    letter-spacing: 2px;
  }
  .card-back .brand-dot {
    width: 16px;
    height: 16px;
    margin-right: 10px;
  }
</style>
</head>
<body>
<main class="canvas">
  <section class="card card-front">
    <div class="site-plan" role="img" aria-label="Faint technical site plan of an athletic facility with track and fields"></div>
    <div class="brand-name"><span class="brand-dot"></span>Solano Field</div>
  </section>

  <section class="card card-back">
    <div class="site-plan" role="img" aria-label="Faint technical site plan of an athletic facility with track and fields"></div>
    <div class="contact">
      <p class="contact-name">Peter L. Vandrell</p>
      <p class="contact-credentials">CFB, CTB</p>
      <address class="contact-address">48317 W 63rd Ave<br>Harlow Ridge,<br>WA 99482</address>
      <p class="contact-lines">C +1 503.555.0147<br>O +1 808.555.0182<br>Peter@fieldlaneco.example</p>
      <a class="contact-website" href="#">WWW.FIELDLANECO.EXAMPLE</a>
    </div>
    <div class="card-divider"></div>
    <div class="brand-name"><span class="brand-dot"></span>Solano Field</div>
  </section>
</main>
</body>
</html>
```